Add words, element to an already make product design

Hi guys,
I m already have the design (attached) which is a wet tissue product. The front main side (about 14cm x 7 cm) is the waves and the brand name Zelfo. However, in this main side, it should contain more words, which are "Khan uot" (mean wet wipe), and the words "Mat lanh" (mean cooling) and "Tinh khiet" (mean purity). "Khan uot" to indicate function of the product, while Mat lanh and Tinh khiet are just marketing term to add.
So yes, the task is quite simple, but I think the key is to choose an appropriate font, color and the location you decide where it should be. You can add any element you want, as long as it look good overall, and those words above, are required to have. More in the attached are few rival from our market, as some example.
Thank you, and wait your idea.

Hi guys, Just to tell you that the main front design will not change. So the waves and the brand name still keep the same. Just adding more words or elements to it. Thank you guys.

```html
<!DOCTYPE html>
<html lang="vi">
<head>
<meta charset="utf-8">
<title>Zelfo – Khăn ướt</title>
<link rel="stylesheet" href="https://fonts.googleapis.com/css2?family=Mulish:wght@300&family=Open+Sans:wght@400;700&display=swap">
<style>
  :root {
    --band-blue: #3182c2;
    --title-blue: #2f7fc1;
    --brand-blue: #4a9fd0;
    --paper: #ffffff;
    --frame: #6b6b6b;
    --wave-light: #d6ecf8;
    --wave-mid: #62b8e6;
    --wave-deep: #2f86cc;
  }
  html, body {
    margin: 0;
    padding: 0;
    width: 1200px;
    height: 977px;
    overflow: hidden;
    background: var(--paper);
  }
  .canvas {
    position: relative;
    width: 1200px;
    height: 977px;
  }
  .pack-front {
    position: absolute;
    left: 213px;
    top: 245px;
    width: 767px;
    height: 401px;
    background: var(--paper);
    outline: 1px solid var(--frame);
    overflow: hidden;
  }
  .wave-art {
    position: absolute;
    inset: 0;
    width: 100%;
    height: 100%;
  }
  .top-band {
    position: absolute;
    left: 0;
    top: 0;
    width: 100%;
    height: 92px;
  }
  .claims {
    position: absolute;
    left: 0;
    top: 20px;
    width: 100%;
    height: 40px;
    font-family: "Open Sans", sans-serif;
    font-weight: 400;
    font-size: 31px;
    letter-spacing: 4px;
    color: var(--paper);
  }
  .claim {
    position: absolute;
    top: 0;
    transform: translateX(-50%);
    white-space: nowrap;
  }
  .claim--cooling { left: 190px; }
  .claim--divider { left: 384px; letter-spacing: 0; font-size: 28px; }
  .claim--purity { left: 569px; }
  .product-type {
    position: absolute;
    left: 274px;
    top: 107px;
    margin: 0;
    font-family: "Mulish", sans-serif;
    font-weight: 300;
    font-size: 53px;
    line-height: 1;
    color: var(--title-blue);
    white-space: nowrap;
  }
  .brand-name {
    position: absolute;
    left: 387px;
    top: 150px;
    transform: translateX(-50%);
    margin: 0;
    font-family: "Open Sans", sans-serif;
    font-weight: 700;
    font-size: 112px;
    line-height: 1;
    color: var(--brand-blue);
    white-space: nowrap;
  }
</style>
</head>
<body>
<div class="canvas">
  <section class="pack-front">
    <svg class="wave-art" viewBox="0 0 767 401" preserveAspectRatio="none" role="img" aria-label="Watercolour blue ocean waves rising from light to deep blue">
      <defs>
        <linearGradient id="waveFill" x1="0" y1="0" x2="0" y2="1">
          <stop offset="0.3" stop-color="#ffffff"/>
          <stop offset="0.48" stop-color="var(--wave-light)"/>
          <stop offset="0.72" stop-color="var(--wave-mid)"/>
          <stop offset="1" stop-color="var(--wave-deep)"/>
        </linearGradient>
      </defs>
      <rect x="0" y="0" width="767" height="401" fill="url(#waveFill)"/>
    </svg>

    <svg class="top-band" viewBox="0 0 767 92" preserveAspectRatio="none" aria-hidden="true">
      <path d="M0 0 H767 V91 Q383 47 0 91 Z" fill="var(--band-blue)"/>
    </svg>

    <div class="claims">
      <span class="claim claim--cooling">Mát lạnh</span>
      <span class="claim claim--divider">|</span>
      <span class="claim claim--purity">Tinhkhiết</span>
    </div>

    <h2 class="product-type">Khănướt</h2>
    <h1 class="brand-name">Zelfo</h1>
  </section>
</div>
</body>
</html>
```